Chiropractic Software Company needs Business Cards

We need a bushiness card design for use at a Chiropractic conference. We build billing, practice management, and medical documentation software. Our product is Halvern Chiropractic Software(Halvern for short). On top of our software we have practice success coaches that coordinate with our chiropractor clients to help them grow their practice and treat more patients. Our logo colors are tried-and-true orange-and-blue. We'd like a sterile white background and a clean layout; organizing the following information: Name, Position/Title, Phone Number, Address, email, and our website. On the backside we'd like our Logo and our slogan, "Your Practice Keystone" and our website(http://www.halvernchiropracticsoftware.example)

Industry/Entity Type

Business

```html
<!DOCTYPE html>
<html lang="en">
<head>
<meta charset="utf-8">
<title>Halvern Business Cards</title>
<link rel="stylesheet" href="https://fonts.googleapis.com/css2?family=Lato:wght@300;400;700&display=swap">
<style>
  :root {
    --page: #e6e7e9;
    --card-dark: #202123;
    --card-white: #fbfbfb;
    --brand-blue: #2a8ccc;
    --brand-orange: #e8612a;
    --ink-light: #ffffff;
    --ink-soft: #e4e4e4;
    --logo-grey: #6d7075;
  }
  * { box-sizing: border-box; margin: 0; padding: 0; }
  html, body {
    width: 1200px; height: 926px; overflow: hidden;
    background: var(--page);
    font-family: "Lato", sans-serif;
  }
  .sheet {
    position: relative; width: 1200px; height: 926px;
  }
  .card {
    position: absolute; left: 250px;
    width: 700px; height: 400px;
    overflow: hidden;
    box-shadow: 0 6px 18px rgba(0,0,0,0.18);
  }
  .card--front { top: 42px; background: var(--card-white); }
  .card--back  { top: 484px; background: var(--card-dark); }

  .front-art { position: absolute; inset: 0; width: 700px; height: 400px; }

  .wordmark {
    display: flex; align-items: center; gap: 10px;
    font-weight: 700; letter-spacing: 3px; text-transform: uppercase;
  }
  .wordmark__dot { border-radius: 50%; background: var(--brand-blue); flex: none; }

  .card--front .wordmark {
    position: absolute; left: 26px; top: 40px;
    font-size: 26px; color: var(--logo-grey);
  }
  .card--front .wordmark__dot { width: 22px; height: 22px; }

  .holder { position: absolute; right: 38px; top: 64px; text-align: right; }
  .holder__name { font-size: 34px; color: var(--ink-light); font-weight: 300; }
  .holder__name strong { font-weight: 700; }
  .holder__title {
    font-size: 15px; color: var(--brand-blue); font-weight: 700;
    letter-spacing: 1.5px; margin-top: 2px;
  }

  .contact {
    position: absolute; left: 390px; top: 262px;
    list-style: none; font-size: 14.5px; color: var(--ink-soft);
    line-height: 20px; letter-spacing: 0.3px;
  }
  .contact li { display: flex; }
  .contact__key {
    width: 20px; flex: none; color: var(--brand-orange); font-weight: 700;
  }
  .contact__cont { padding-left: 20px; }

  .card--back .wordmark {
    position: absolute; left: 0; right: 0; top: 130px;
    justify-content: center; font-size: 52px; color: var(--ink-soft);
    gap: 16px;
  }
  .card--back .wordmark__dot { width: 40px; height: 40px; background: var(--brand-orange); }
  .slogan {
    position: absolute; left: 0; right: 0; top: 222px;
    text-align: center; font-size: 34px; font-weight: 300;
    color: var(--brand-blue); letter-spacing: 1px;
  }
</style>
</head>
<body>
<main class="sheet">
  <section class="card card--front" aria-label="Business card front">
    <svg class="front-art" viewBox="0 0 700 400" aria-hidden="true">
      <path d="M300 0 Q160 150 70 400 L700 400 L700 0 Z" fill="var(--brand-blue)"/>
      <path d="M345 0 Q205 160 128 400 L700 400 L700 0 Z" fill="var(--card-dark)"/>
      <path d="M350 145 Q250 250 205 400 L320 400 Q318 260 350 145 Z" fill="var(--brand-orange)"/>
    </svg>

    <div class="wordmark"><span class="wordmark__dot"></span>Halvern</div>

    <div class="holder">
      <p class="holder__name">Aren <strong>Velcott</strong></p>
      <p class="holder__title">TITLE HERE</p>
    </div>

    <ul class="contact">
      <li><span class="contact__key">P</span>: +123 555 0147</li>
      <li><span class="contact__key">W</span>: halvernchiropracticsoftware.example</li>
      <li><span class="contact__key">E</span>: yourname@halverncs.example</li>
      <li><span class="contact__key">A</span>: Street address goes here,</li>
      <li class="contact__cont">Suite #410, Orin Bldg, NY 82490</li>
    </ul>
  </section>

  <section class="card card--back" aria-label="Business card back">
    <div class="wordmark"><span class="wordmark__dot"></span>Halvern</div>
    <p class="slogan">Your Practice Keystone</p>
  </section>
</main>
</body>
</html>
```